Home Security Company Business Card

Looking for a eye catching business card that is non traditional and stands out but yet still looks professional. It should include all the pertinent information such as name, title, address, telephone, e-mail, website address should definitely stand out and then finally the logo.

Target Market(s)

Residential and Commercial accounts mostly upscale accounts

Industry/Entity Type

Security

Contact Information for Business Card

Name
Title
Address
Office #
Cell #
E-mail
Website

Font styles to use
Serif
Sans Serif

Requirements
Must have
• Logo, two sided color configuration
Nice to have
• You decide
Should not have
• There really aren't any.

```html
<!DOCTYPE html>
<html lang="en">
<head>
<meta charset="utf-8">
<title>Ironward Security Systems – Business Card</title>
<link rel="stylesheet" href="https://fonts.googleapis.com/css2?family=Arimo:wght@400;700&display=swap">
<style>
  :root {
    --backdrop: #4a413c;
    --card: #1b1b1c;
    --brand-red: #8e1c12;
    --name-red: #a3231a;
    --gold: #d9a131;
    --ink: #f1f1f1;
    --rule: #e9e9e9;
  }
  * { box-sizing: border-box; margin: 0; padding: 0; }
  html, body {
    width: 1200px; height: 787px; overflow: hidden;
    background: var(--backdrop);
    font-family: "Arimo", Arial, sans-serif;
  }
  .canvas { position: relative; width: 1200px; height: 787px; }
  .card {
    position: absolute;
    width: 540px; height: 309px;
    background: var(--card);
    border-radius: 4px;
    box-shadow: 0 10px 24px rgba(0,0,0,.35);
  }
  .card--front { left: 40px; top: 110px; }
  .card--back { left: 620px; top: 368px; }

  .brand {
    position: absolute;
    display: flex; align-items: center; gap: 10px;
    color: var(--brand-red);
    font-weight: 700;
    letter-spacing: .04em;
    text-transform: uppercase;
    line-height: 1.05;
  }
  .brand__mark {
    width: 16px; height: 16px; border-radius: 50%;
    background: var(--gold); flex: none;
  }
  .card--front .brand { left: 150px; top: 110px; font-size: 26px; }
  .card--back .brand { right: 36px; top: 74px; font-size: 20px; }

  .front__web {
    position: absolute; left: 0; right: 0; top: 230px;
    text-align: center;
    color: var(--ink); font-size: 13px; letter-spacing: .35em;
  }

  .person { position: absolute; left: 30px; top: 128px; }
  .person__name { color: var(--name-red); font-size: 20px; }
  .person__title { color: var(--gold); font-size: 14px; margin-top: 2px; }
  .rule {
    position: absolute; left: 98px; right: 30px; top: 170px;
    height: 1px; background: var(--rule);
  }
  .address {
    position: absolute; left: 30px; top: 186px;
    color: var(--ink); font-size: 13px; line-height: 1.55; font-style: normal;
  }
  .contact {
    position: absolute; list-style: none;
    color: var(--ink); font-size: 15px; line-height: 1;
  }
  .contact li { display: flex; align-items: center; gap: 9px; margin-bottom: 9px; }
  .contact svg { width: 14px; height: 14px; fill: var(--brand-red); flex: none; }
  .contact--phones { left: 200px; top: 204px; }
  .contact--online { left: 360px; top: 250px; }
</style>
</head>
<body>
<main class="canvas">
  <section class="card card--front" aria-label="Card front">
    <div class="brand"><span class="brand__mark"></span><span>Ironward<br>Security Systems</span></div>
    <p class="front__web">www.ironward.com</p>
  </section>

  <section class="card card--back" aria-label="Card back">
    <div class="brand"><span class="brand__mark"></span><span>Ironward<br>Security Systems</span></div>

    <div class="person">
      <p class="person__name">Mark Ellison</p>
      <p class="person__title">President</p>
    </div>
    <div class="rule"></div>

    <address class="address">2710 Harbor Lane<br>Glen Cove, NY 11542</address>

    <ul class="contact contact--phones">
      <li>
        <svg viewBox="0 0 24 24" aria-hidden="true"><path d="M6.6 10.8a15.1 15.1 0 0 0 6.6 6.6l2.2-2.2a1 1 0 0 1 1-.25 11.4 11.4 0 0 0 3.6.57 1 1 0 0 1 1 1V20a1 1 0 0 1-1 1A17 17 0 0 1 3 4a1 1 0 0 1 1-1h3.5a1 1 0 0 1 1 1c0 1.25.2 2.45.57 3.57a1 1 0 0 1-.25 1z"/></svg>
        <span>555 0142 7781</span>
      </li>
      <li>
        <svg viewBox="0 0 24 24" aria-hidden="true"><path d="M7 1h10a2 2 0 0 1 2 2v18a2 2 0 0 1-2 2H7a2 2 0 0 1-2-2V3a2 2 0 0 1 2-2zm0 3v14h10V4zm5 15.5a1.2 1.2 0 1 0 0 2.4 1.2 1.2 0 0 0 0-2.4z"/></svg>
        <span>555 0198 3364</span>
      </li>
    </ul>

    <ul class="contact contact--online">
      <li>
        <svg viewBox="0 0 24 24" aria-hidden="true"><path d="M2 5h20v14H2zm2 2v.5l8 5 8-5V7l-8 5z"/></svg>
        <span>mark@ironward.com</span>
      </li>
      <li>
        <svg viewBox="0 0 24 24" aria-hidden="true"><path d="M12 2a10 10 0 1 0 0 20 10 10 0 0 0 0-20zm-1 17.9A8 8 0 0 1 4.1 11H7c.1 3.2 1.5 6.4 4 8.9zM7 9H4.3A8 8 0 0 1 11 4.1C8.7 6.2 7.3 7.5 7 9zm6 10.9c2.5-2.5 3.9-5.7 4-8.9h2.9A8 8 0 0 1 13 19.9zM17 9c-.3-1.5-1.7-2.8-4-4.9A8 8 0 0 1 19.7 9zM9 11h6c-.1 2.8-1.1 5.3-3 7.2-1.9-1.9-2.9-4.4-3-7.2zm0-2c.3-1.3 1.3-2.6 3-4.1 1.7 1.5 2.7 2.8 3 4.1z"/></svg>
        <span>www.ironward.com</span>
      </li>
    </ul>
  </section>
</main>
</body>
</html>
```